Heronby Mortgage Capital Business Card

We need a business card design for our mortgage servicing company. In addition to servicing the loans of homeowners, we help homeowners with purchasing their homes and any mortgage refinancing. We would like to see designs that use the colors in the logo attached below (gold-ish yellow and navy blue), and any other design you deem fit! The design should communicate a simpler life with smart mortgages provided by Heronby.

```html
<!DOCTYPE html>
<html lang="en">
<head>
<meta charset="utf-8">
<title>Heronby Mortgage Capital – Business Card</title>
<link rel="stylesheet" href="https://fonts.googleapis.com/css2?family=Lora:wght@400;700&display=swap">
<style>
  :root {
    --backdrop: #b3b3b3;
    --gold: #dfb13f;
    --navy: #2a2457;
    --ink: #1a1a1a;
    --paper: #ffffff;
  }
  * { box-sizing: border-box; margin: 0; padding: 0; }
  html, body {
    width: 1154px;
    height: 1200px;
    overflow: hidden;
    background: var(--backdrop);
    font-family: "Lora", Georgia, serif;
  }
  .canvas { position: relative; width: 1154px; height: 1200px; }

  .card {
    position: absolute;
    left: 191px;
    width: 771px;
    height: 441px;
    border-radius: 30px;
    box-shadow: 0 6px 8px rgba(0, 0, 0, 0.12);
  }
  .card--front { top: 138px; background: var(--gold); }
  .card--back  { top: 620px; background: var(--paper); }

  .wordmark {
    position: absolute;
    left: 0;
    width: 100%;
    text-align: center;
    font-weight: 700;
    font-size: 50px;
    line-height: 1;
    color: var(--navy);
    letter-spacing: 0.5px;
  }
  .card--front .wordmark { top: 198px; }
  .card--back  .wordmark { top: 90px; }

  .person {
    position: absolute;
    top: 203px;
    left: 0;
    width: 100%;
    text-align: center;
    color: var(--navy);
  }
  .person__name {
    font-weight: 700;
    font-size: 27px;
    letter-spacing: 0.3px;
    line-height: 1.2;
  }
  .person__role {
    margin-top: 4px;
    font-size: 17px;
    color: var(--ink);
    letter-spacing: 0.5px;
  }

  .divider {
    position: absolute;
    height: 2px;
    background: var(--ink);
  }
  .divider--left  { left: 119px; top: 296px; width: 196px; }
  .divider--right { left: 456px; top: 293px; width: 196px; }

  .contact-icons {
    position: absolute;
    left: 323px;
    top: 280px;
    width: 128px;
    height: 28px;
  }

  .contact-list {
    position: absolute;
    top: 323px;
    left: 0;
    width: 100%;
    list-style: none;
    text-align: center;
    font-size: 17.5px;
    line-height: 25.5px;
    color: var(--ink);
    letter-spacing: 0.4px;
  }
</style>
</head>
<body>
<main class="canvas">

  <section class="card card--front" aria-label="Card front">
    <p class="wordmark">Heronby Mortgage</p>
  </section>

  <section class="card card--back" aria-label="Card back">
    <p class="wordmark">Heronby Mortgage</p>

    <div class="person">
      <h1 class="person__name">JONATHAN SMITH</h1>
      <p class="person__role">MANAGING DIRECTOR</p>
    </div>

    <span class="divider divider--left"></span>
    <svg class="contact-icons" viewBox="0 0 128 28" aria-hidden="true">
      <g fill="var(--navy)">
        <circle cx="14" cy="14" r="14"/>
        <circle cx="44" cy="14" r="14"/>
        <circle cx="76" cy="14" r="14"/>
        <circle cx="109" cy="14" r="14"/>
      </g>
      <g fill="none" stroke="var(--gold)" stroke-width="1.6" stroke-linecap="round" stroke-linejoin="round">
        <!-- phone -->
        <path d="M8.5 8.5 l2.5-1 2 3.5 -1.6 1.3 q1.2 2.6 3.6 3.8 l1.4-1.5 3.4 2 -1 2.5 q-6 0.5 -10.3-10.6z"/>
        <!-- envelope -->
        <rect x="37" y="9" width="14" height="10" rx="1"/>
        <path d="M37.5 9.5 L44 15 L50.5 9.5"/>
        <!-- globe -->
        <circle cx="76" cy="14" r="7"/>
        <ellipse cx="76" cy="14" rx="3" ry="7"/>
        <path d="M69 14 H83 M70 10.5 H82 M70 17.5 H82"/>
      </g>
      <!-- location pin -->
      <path fill="var(--gold)" d="M109 6.5 a5.5 5.5 0 0 1 5.5 5.5 c0 4 -5.5 9.5 -5.5 9.5 s-5.5-5.5 -5.5-9.5 a5.5 5.5 0 0 1 5.5-5.5z"/>
      <circle cx="109" cy="12" r="2" fill="var(--navy)"/>
    </svg>
    <span class="divider divider--right"></span>

    <ul class="contact-list">
      <li>044-123 456 789</li>
      <li>info@webname.com</li>
      <li>www.websitename.com</li>
      <li>421, Address line goes here&nbsp; 45452, Country name</li>
    </ul>
  </section>

</main>
</body>
</html>
```